Rise As Captain Book Cover Design

Book Cover Design Brief
Book Title
Rise As Captain
Subtitle
The 10 Quiet Habits of Remarkable Command
Author
Orwen Dalquist
Overview
This book is about leadership that starts within.
Most leadership books focus on tactics or management strategies. This book focuses on the inner disciplines that create powerful leaders — mindset, integrity, focus, empathy, professionalism, honesty, and self-respect.
The tone of the book is bold, direct, confident, and transformational.
This is not a soft or corporate leadership book. It is a call to step up and become the leader you are capable of becoming.
The cover should feel:
• Powerful
• Professional
• Transformational
• Premium
• Memorable
Think best-selling leadership book, not a generic business book.
Target Audience
Business owners
Managers
Entrepreneurs
Team leaders
Professionals who want to grow as leaders
Most readers are ambitious professionals who want to level up their leadership and life.
Design Direction
The design should communicate:
Strength. Discipline. Leadership. Personal transformation.
Avoid cliché leadership visuals like:
• Handshakes
• Office buildings
• Corporate stock imagery
• Teams sitting around tables
The design should feel iconic, bold, and timeless.
Think about covers of successful leadership books such as:
Copper Rituals
Total Stewardship
Won't Break Now
Begin From Purpose
The 36 Rules of Sway
These covers are simple, powerful, and recognizable even at small sizes.
Typography
The title RISE AS CAPTAIN should be:
• Bold
• Strong
• Dominant on the cover
• Easy to read even at small sizes (important for Vellora thumbnails)
The subtitle should be clean and secondary to the title.
The overall typography should feel strong, modern, and premium.
Color Direction
Designers are free to explore colors, but the cover should feel strong and premium, not playful.
Colors that often work well for leadership books include:
Black
Gold
White
Deep blue
Dark red
High contrast and clarity are important.
Style
Preferred style:
• Clean
• Modern
• Minimal
• Strong contrast
Avoid clutter and overly busy designs.
The goal is to create a cover that feels powerful and professional at first glance.
Deliverables
Front cover design for a leadership book.
Final files should include:
• High resolution artwork
• Editable source files
• Print-ready version suitable for publishing
Goal of the Cover
When someone sees this book on Vellora or in a bookstore, they should immediately think:
“This looks like a serious leadership book.”
The design should feel like it belongs next to books by authors such as:
Marcus Thorley
Brandt Osgood
Peter Hollis
Nolan Fairbrook
A strong, confident cover that attracts leaders who want to grow and perform at a higher level.
Target Market(s)
Business Owners and High level managers
Look and feel
Each slider illustrates characteristics of the customer's brand and the style your logo design should communicate.

```html
<!DOCTYPE html>
<html lang="en">
<head>
<meta charset="utf-8">
<title>Rise As Captain — Book Cover</title>
<link rel="stylesheet" href="https://fonts.googleapis.com/css2?family=Anton&family=Arimo:wght@700&display=swap">
<style>
  :root {
    --page-bg: #ffffff;
    --cover-bg: #201f20;
    --gold-dark: #6a4e22;
    --gold-mid: #a47c40;
    --gold-light: #e5b063;
    --ink-white: #ffffff;
  }
  html, body {
    margin: 0;
    padding: 0;
    width: 1200px;
    height: 1200px;
    overflow: hidden;
    background: var(--page-bg);
  }
  .canvas {
    display: block;
    width: 1200px;
    height: 1200px;
  }
  .cover-panel { fill: var(--cover-bg); }
  .title-line {
    font-family: "Anton", "Oswald", sans-serif;
    fill: url(#titleGold);
  }
  .title-line--top { font-size: 284px; }
  .title-line--bottom { font-size: 272px; }
  .subtitle-line,
  .author-name {
    font-family: "Arimo", "Helvetica Neue", Arial, sans-serif;
    font-weight: 700;
    fill: var(--ink-white);
  }
  .subtitle-line--top { font-size: 39px; }
  .subtitle-line--bottom { font-size: 47px; }
  .author-name { font-size: 47px; }
</style>
</head>
<body>
<svg class="canvas" viewBox="0 0 1200 1200" xmlns="http://www.w3.org/2000/svg" role="img" aria-label="Rise As Captain book cover by Orwen Dalquist">
  <defs>
    <linearGradient id="titleGold" gradientUnits="userSpaceOnUse" x1="327" y1="784" x2="916" y2="220">
      <stop offset="0" stop-color="#6a4e22" style="stop-color: var(--gold-dark)"/>
      <stop offset="0.5" stop-color="#a47c40" style="stop-color: var(--gold-mid)"/>
      <stop offset="1" stop-color="#e5b063" style="stop-color: var(--gold-light)"/>
    </linearGradient>
  </defs>

  <rect class="cover-panel" x="286" y="96" width="666" height="997"/>

  <text class="title-line title-line--top" x="335" y="466" textLength="575" lengthAdjust="spacingAndGlyphs">RISE AS</text>
  <text class="subtitle-line subtitle-line--top" x="332" y="523" textLength="559" lengthAdjust="spacing">THE 10 QUIET HABITS OF</text>
  <text class="title-line title-line--bottom" x="327" y="784" textLength="589" lengthAdjust="spacingAndGlyphs">CAPTAIN</text>
  <text class="subtitle-line subtitle-line--bottom" x="621" y="859" text-anchor="middle">REMARKABLE COMMAND</text>

  <text class="author-name" x="625" y="1059" text-anchor="middle">ORWEN DALQUIST</text>
</svg>
</body>
</html>
```